Business card / stationery design
Pemberton Hale Warrick
Project: Business card / stationery design
Business card / stationery design - Engineering
Creative Brief
Use specific fonts
Gill Sans MT, Calibri, Corbel, Lucida Sans UC or similar
Professional
Derek R. Pemberton, P.E., LEED A.P., CPMP
Principal
4738 E. Harrowgate Ave., Suite C-212B, Springfield, Missouri 65809
dpemberton@pembertonhalewarrick.example
www.pembertonhalewarrick.example
We would like to use only the logo from the attached file. We like the current color arrangement, but would be interested in seeing it in other colors. Also the slightly gray color behind the logo should just be white or whatever the background color is. A couple of examples are attached. The main text adjacent to the logo should read: Pemberton Hale Warrick. Secondary text will be similar to: Engineering & Energy Services.
We are interested in your ideas.

```html
<!DOCTYPE html>
<html lang="en">
<head>
<meta charset="utf-8">
<title>Pemberton Hale Warrick – Business Cards</title>
<link rel="stylesheet" href="https://fonts.googleapis.com/css2?family=Cabin:wght@400;600&family=Cormorant+Garamond:wght@600&display=swap">
<style>
  :root {
    --bg: #f1f1f1;
    --card-white: #ffffff;
    --blue: #1f5fa8;
    --blue-dark: #12427e;
    --green: #6ab52c;
    --green-dark: #3f8c22;
    --ink: #2a2a2a;
    --muted: #6b6b6b;
  }
  * { margin: 0; padding: 0; box-sizing: border-box; }
  html, body { width: 1200px; height: 326px; overflow: hidden; background: var(--bg); }
  body { position: relative; font-family: "Cabin", "Gill Sans", sans-serif; color: var(--ink); }

  .card {
    position: absolute; top: 84px; width: 228px; height: 156px;
    border-radius: 10px; overflow: hidden;
    box-shadow: 0 3px 8px rgba(0,0,0,.18);
  }
  .card--contact { left: 67px; background: var(--card-white); }
  .card--white { left: 343px; background: var(--card-white); }
  .card--green { left: 629px; background: linear-gradient(135deg, #8fcc3c, var(--green-dark)); color: #fff; }
  .card--blue { left: 905px; background: linear-gradient(135deg, #3c83d1, var(--blue-dark)); color: #fff; }

  /* contact card */
  .side-strip { position: absolute; left: 0; top: 0; bottom: 0; width: 12px;
    background: linear-gradient(180deg, var(--green) 0 38%, var(--blue) 38% 100%); }
  .contact-brand { position: absolute; left: 22px; top: 14px; display: flex; align-items: center; gap: 5px; }
  .contact-brand .mark { width: 14px; height: 14px; background: var(--blue); }
  .contact-brand .name { font-family: "Cormorant Garamond", serif; font-weight: 600; font-size: 9px;
    line-height: 1.05; color: var(--blue-dark); text-transform: uppercase; letter-spacing: .5px; width: 60px; }
  .contact-tagline { position: absolute; left: 98px; top: 16px; font-size: 5px; color: var(--muted); line-height: 1.3; width: 40px; }
  .divider { position: absolute; left: 138px; top: 12px; width: 1px; height: 24px; background: #c9c9c9; }
  .person { position: absolute; left: 146px; top: 13px; }
  .person .full { font-size: 9px; color: var(--blue); font-weight: 600; }
  .person .creds { font-size: 5px; color: var(--muted); }
  .person .role { font-size: 5px; color: var(--muted); }
  .address { position: absolute; left: 22px; top: 60px; width: 110px; font-size: 5px; line-height: 1.45; color: var(--ink); }
  .address .label { color: var(--blue); font-weight: 600; }
  .channels { position: absolute; left: 22px; bottom: 14px; font-size: 5px; line-height: 1.6; color: var(--ink); }
  .channels.right { left: 118px; }

  /* brand cards */
  .brand { position: absolute; left: 0; right: 0; top: 34px; text-align: center; }
  .brand .mark { width: 30px; height: 30px; margin: 0 auto 8px; background: var(--green); }
  .card--green .brand .mark, .card--blue .brand .mark { background: #fff; }
  .brand .name { font-family: "Cormorant Garamond", serif; font-weight: 600; font-size: 13px;
    letter-spacing: 1.2px; text-transform: uppercase; color: var(--blue-dark); }
  .card--green .brand .name, .card--blue .brand .name { color: #fff; }
  .brand .tagline { font-size: 5.5px; margin-top: 2px; color: var(--muted); }
  .card--green .brand .tagline, .card--blue .brand .tagline { color: rgba(255,255,255,.85); }
  .web { position: absolute; left: 0; right: 0; bottom: 16px; text-align: center; font-size: 6.5px; color: var(--muted); }
  .card--green .web, .card--blue .web { color: #fff; }
</style>
</head>
<body>

<section class="card card--contact" aria-label="Contact card">
  <div class="side-strip"></div>
  <div class="contact-brand">
    <span class="mark"></span>
    <span class="name">Pemberton Hale Warrick</span>
  </div>
  <p class="contact-tagline">Engineering &amp; Energy Services</p>
  <div class="divider"></div>
  <div class="person">
    <p class="full">Derek R. Pemberton</p>
    <p class="creds">P.E., LEED A.P., CPMP</p>
    <p class="role">Principal</p>
  </div>
  <p class="address">
    <span class="label">Office</span><br>
    4738 E. Harrowgate Ave.,<br>
    Suite C-212B<br>
    Springfield, Missouri 65809
  </p>
  <p class="channels">T 417.555.0142<br>F 417.555.0143</p>
  <p class="channels right">dpemberton@pembertonhalewarrick.example<br>www.pembertonhalewarrick.example</p>
</section>

<section class="card card--white" aria-label="Brand card, white">
  <div class="brand">
    <div class="mark"></div>
    <p class="name">Pemberton Hale Warrick</p>
    <p class="tagline">Engineering &amp; Energy Services</p>
  </div>
  <p class="web">www.pembertonhalewarrick.example</p>
</section>

<section class="card card--green" aria-label="Brand card, green">
  <div class="brand">
    <div class="mark"></div>
    <p class="name">Pemberton Hale Warrick</p>
    <p class="tagline">Engineering &amp; Energy Services</p>
  </div>
  <p class="web">www.pembertonhalewarrick.example</p>
</section>

<section class="card card--blue" aria-label="Brand card, blue">
  <div class="brand">
    <div class="mark"></div>
    <p class="name">Pemberton Hale Warrick</p>
    <p class="tagline">Engineering &amp; Energy Services</p>
  </div>
  <p class="web">www.pembertonhalewarrick.example</p>
</section>

</body>
</html>
```